Fresh new and cool frozen burger box! Come be a part of an amazing project!

Crust Fries and Melts restaurant is expanding into the frozen foods market!
please check out our website to understand the vibe of the company
https://grillvexa.ca
this is a line of premium Halal meat, we want to stress our top-notch quality.
we like the orange colours so see what you can do with them. (maybe white and orange combo)
you have lots of creative freedom here, feel free to use the burger photo I am attaching or any image off the website.
logo should be nice and visible.
we want this packaging to really stand out and be special.
Come be a part of an amazing project!
Target Market(s)
Muslim Flails, looking of a quality meat burger. mostly already familiar with our brand
Industry/Entity Type
Frozen food
Look and feel

```html
<!DOCTYPE html>
<html lang="en">
<head>
<meta charset="utf-8">
<title>Grillvexa BBQ Chicken Burger Box</title>
<link href="https://fonts.googleapis.com/css2?family=Lilita+One&family=Open+Sans:wght@600;800&display=swap" rel="stylesheet">
<style>
  :root {
    --canvas: #f2f2f2;
    --orange-deep: #e0642a;
    --orange-mid: #ec8a2c;
    --orange-light: #f2a33a;
    --red-band: #d0303a;
    --red-dark: #a9232c;
    --ink: #3a3a3a;
    --white: #ffffff;
  }
  * { margin: 0; padding: 0; box-sizing: border-box; }
  html, body { width: 1200px; height: 800px; overflow: hidden; background: var(--canvas); }
  .box-net {
    position: absolute; left: 220px; top: 70px; width: 760px; height: 660px;
    box-shadow: 0 14px 40px rgba(0,0,0,.18);
  }
  .lid { position: absolute; left: 0; top: 0; width: 760px; height: 520px; overflow: hidden; }
  .lid-art { position: absolute; inset: 0; }
  .brand-name {
    font-family: "Open Sans", sans-serif; font-weight: 800; font-size: 44px; line-height: 1;
    color: var(--white); display: flex; align-items: center; gap: 12px;
  }
  .brand-square { width: 18px; height: 18px; background: var(--white); display: inline-block; }
  .lid .brand-name { position: absolute; right: 40px; top: 44px; }
  .nutrition { position: absolute; left: 28px; top: 28px; display: flex; gap: 8px; }
  .nutrient {
    width: 62px; height: 76px; border: 2px solid rgba(255,255,255,.85); border-radius: 30px 30px 8px 8px;
    display: flex; flex-direction: column; align-items: center; justify-content: space-between;
    padding: 10px 4px 6px; color: var(--white);
    font-family: "Open Sans", sans-serif; font-weight: 600; font-size: 10px; line-height: 1.15; text-align: center;
  }
  .nutrient .pct {
    background: var(--white); color: var(--orange-deep); border-radius: 10px; width: 46px;
    font-weight: 800; font-size: 12px; padding: 2px 0;
  }
  .product-title { position: absolute; left: 36px; top: 150px; color: var(--white); }
  .product-flavour {
    font-family: "Lilita One", sans-serif; font-size: 40px; line-height: 1;
    -webkit-text-stroke: 2px var(--ink); paint-order: stroke fill;
  }
  .product-name {
    font-family: "Lilita One", sans-serif; font-size: 104px; line-height: .95;
    -webkit-text-stroke: 3px var(--ink); paint-order: stroke fill;
  }
  .seals { position: absolute; left: 60px; top: 330px; display: flex; flex-direction: column; gap: 22px; }
  .seal { width: 110px; height: 70px; }
  .side-band {
    position: absolute; left: 0; top: 520px; width: 760px; height: 140px;
    background: linear-gradient(180deg, var(--red-band), var(--red-dark));
    display: flex; align-items: center; justify-content: center;
  }
  .side-band .brand-name { font-size: 52px; }
</style>
</head>
<body>
  <main class="box-net">
    <section class="lid">
      <svg class="lid-art" width="760" height="520" viewBox="0 0 760 520">
        <defs>
          <linearGradient id="orangeField" x1="0" y1="0" x2="0.6" y2="1">
            <stop offset="0" stop-color="#e0642a"/>
            <stop offset="1" stop-color="#f2a33a"/>
          </linearGradient>
          <linearGradient id="photoTones" x1="0" y1="0" x2="0" y2="1">
            <stop offset="0" stop-color="#6d7f96"/>
            <stop offset="0.35" stop-color="#8a8f98"/>
            <stop offset="0.55" stop-color="#d9a065"/>
            <stop offset="0.8" stop-color="#b8622f"/>
            <stop offset="1" stop-color="#8b5a35"/>
          </linearGradient>
        </defs>
        <rect width="760" height="520" fill="url(#orangeField)"/>
        <path d="M440 0 C 360 60, 460 130, 420 200 C 380 270, 300 300, 320 400 C 335 470, 380 500, 400 520 L 760 520 L 760 0 Z"
              fill="#f5b04a" opacity=".6"/>
        <g role="img" aria-label="Photo of a grilled BBQ chicken burger on a sesame bun with cheese, tomato and lettuce on a wooden board">
          <path d="M460 0 C 380 60, 480 130, 440 200 C 400 270, 320 300, 340 400 C 355 470, 400 500, 420 520 L 760 520 L 760 0 Z"
                fill="url(#photoTones)"/>
        </g>
      </svg>

      <div class="nutrition">
        <div class="nutrient"><span>Energy<br>245kcal</span><span class="pct">12%</span></div>
        <div class="nutrient"><span>Fat<br>12g</span><span class="pct">14%</span></div>
        <div class="nutrient"><span>Satura-<br>ted Fat 2g</span><span class="pct">10%</span></div>
        <div class="nutrient"><span>Sugars<br>4g</span><span class="pct">8%</span></div>
        <div class="nutrient"><span>Salt<br>0.2g</span><span class="pct">9%</span></div>
      </div>

      <div class="product-title">
        <div class="product-flavour">BBQ CHICKEN</div>
        <div class="product-name">Burger</div>
      </div>

      <div class="seals">
        <svg class="seal" viewBox="0 0 110 70"><polygon points="55,3 105,20 105,50 55,67 5,50 5,20" fill="none" stroke="#fff" stroke-width="2"/></svg>
        <svg class="seal" viewBox="0 0 110 70"><polygon points="20,3 90,3 105,35 90,67 20,67 5,35" fill="none" stroke="#fff" stroke-width="2"/></svg>
      </div>

      <div class="brand-name"><span class="brand-square"></span>Grillvexa</div>
    </section>

    <section class="side-band">
      <div class="brand-name"><span class="brand-square"></span>Grillvexa</div>
    </section>
  </main>
</body>
</html>
```